Business Card/Letterhead Design

We have our Logo, we simply need it cleaned up. Along with a letterhead design. It's pretty simple really.
Instead of the "Corporation" beside the logo. We need it to say "Limited" just under the logo between the "F" and the "Y"
The letter head has to have our address. 2745 Halvorby Crescent Mississauga, ON L4W 3K8 Canada
Reason: I have been called out of town until Monday of next week.
Business
Contact Information for Business Card
2745 Halvorby Crescent Mississauga, ON L4W 3K8 Canada

```html
<!DOCTYPE html>
<html lang="en">
<head>
<meta charset="utf-8">
<title>Parkline Limited – Business Card and Letterhead</title>
<link rel="stylesheet" href="https://fonts.googleapis.com/css2?family=Open+Sans:wght@400;600;700&display=swap">
<style>
  :root {
    --backdrop: #8e8e8e;
    --paper: #ffffff;
    --brand-blue: #2b3590;
    --brand-blue-deep: #1f2772;
    --brand-blue-light: #3a46a8;
    --copper: #b9702c;
    --copper-light: #d89a5a;
    --ink-light: #ffffff;
  }
  * { margin: 0; padding: 0; box-sizing: border-box; }
  html, body { width: 1200px; height: 900px; overflow: hidden; }
  body {
    background: var(--backdrop);
    font-family: "Open Sans", Arial, sans-serif;
    position: relative;
  }

  /* Business card */
  .business-card {
    position: absolute;
    left: 68px; top: 470px;
    width: 500px; height: 310px;
    border-radius: 20px;
    overflow: hidden;
    background: var(--paper);
    box-shadow: 0 10px 24px rgba(0,0,0,.28);
  }
  .card-top { position: relative; height: 170px; }
  .brand-mark {
    position: absolute;
    display: flex; align-items: center; gap: 12px;
    color: var(--brand-blue);
    font-weight: 600;
  }
  .card-top .brand-mark { left: 36px; top: 68px; font-size: 40px; }
  .brand-disc {
    width: 52px; height: 52px; border-radius: 50%;
    border: 3px solid var(--copper);
    flex: none;
  }
  .card-holder { position: absolute; right: 26px; top: 14px; text-align: right; }
  .holder-name { color: var(--copper); font-size: 16px; font-weight: 600; }
  .holder-role { color: var(--brand-blue); font-size: 11px; }
  .copper-rule {
    height: 8px;
    background: linear-gradient(180deg, var(--copper-light), var(--copper));
    border-bottom: 2px solid #e6e6e6;
  }
  .card-bottom {
    height: 132px;
    background: linear-gradient(180deg, var(--brand-blue-light), var(--brand-blue-deep));
    padding: 20px 32px;
    position: relative;
    color: var(--ink-light);
    font-size: 15px;
    line-height: 18px;
  }
  .contact-list { list-style: none; }
  .contact-list li { display: flex; gap: 8px; }
  .contact-list svg { width: 14px; height: 14px; flex: none; margin-top: 2px; }
  .contact-indent { padding-left: 22px; }
  .social-links { position: absolute; right: 30px; top: 52px; display: flex; gap: 4px; }
  .social-square { width: 18px; height: 18px; background: var(--copper); border-radius: 2px; }

  /* Letterhead */
  .letterhead {
    position: absolute;
    left: 605px; top: 60px;
    width: 550px; height: 780px;
    background: var(--paper);
    box-shadow: 0 10px 24px rgba(0,0,0,.28);
  }
  .letterhead .brand-mark { left: 24px; top: 40px; font-size: 27px; gap: 8px; }
  .letterhead .brand-disc { width: 34px; height: 34px; border-width: 2px; }
  .letterhead-footer { position: absolute; left: 0; right: 0; bottom: 0; }
  .letterhead-footer .copper-rule { height: 6px; }
  .footer-band {
    height: 58px;
    background: linear-gradient(180deg, var(--brand-blue-light), var(--brand-blue-deep));
    color: var(--ink-light);
    font-size: 10px; font-weight: 600;
    letter-spacing: 1.5px;
    display: flex; align-items: center; justify-content: center;
  }
</style>
</head>
<body>

<section class="business-card" aria-label="Business card">
  <div class="card-top">
    <div class="brand-mark"><span class="brand-disc"></span>Parkline Limited</div>
    <div class="card-holder">
      <p class="holder-name">Dana Whitcombe</p>
      <p class="holder-role">Director</p>
    </div>
  </div>
  <div class="copper-rule"></div>
  <div class="card-bottom">
    <ul class="contact-list">
      <li>
        <svg viewBox="0 0 16 16" aria-hidden="true"><path d="M3 1l3 3-2 2c1 2 3 4 5 5l2-2 3 3-2 3C6 15 1 10 1 3z" fill="var(--copper)"/></svg>
        405 555 0148
      </li>
      <li>
        <svg viewBox="0 0 16 16" aria-hidden="true"><rect x="1" y="4" width="14" height="10" fill="var(--copper)"/><path d="M1 4l7 6 7-6" stroke="#fff" stroke-width="1.2" fill="none"/></svg>
        talent@parklinelimited.com
      </li>
      <li>
        <svg viewBox="0 0 16 16" aria-hidden="true"><circle cx="8" cy="8" r="6.5" stroke="var(--copper)" stroke-width="1.5" fill="none"/><path d="M1.5 8h13M8 1.5c-3 3-3 10 0 13M8 1.5c3 3 3 10 0 13" stroke="var(--copper)" stroke-width="1.2" fill="none"/></svg>
        www.parklinelimited.com
      </li>
      <li>
        <svg viewBox="0 0 16 16" aria-hidden="true"><path d="M8 1l7 7h-2v7H9v-4H7v4H3V8H1z" fill="var(--copper)"/></svg>
        2745 Halvorby Crescent Mississauga,
      </li>
      <li class="contact-indent">ON L4W 3K8 Canada</li>
    </ul>
    <div class="social-links" aria-label="Social media links">
      <span class="social-square"></span>
      <span class="social-square"></span>
    </div>
  </div>
</section>

<section class="letterhead" aria-label="Letterhead">
  <div class="brand-mark"><span class="brand-disc"></span>Parkline Limited</div>
  <footer class="letterhead-footer">
    <div class="copper-rule"></div>
    <div class="footer-band">2745 Halvorby Crescent Mississauga, ON L4W 3K8 Canada</div>
  </footer>
</section>

</body>
</html>
```